Business Card Design for my Real Estate Investing Company

This is for a Real Estate Investing Company that will be serving the Las Vegas Valley. Id like the following slogan included: "Investing in Our Community" I have attached my logo. You will see the color tones I'm interested in..in my logo. I would like the card to be double-sided with a modern, professional look.
Target Market(s)
Homeowners, banks, real estate industry
Industry/Entity Type
Real Estate
Contact Information for Business Card
name: Dale Pruitt
position: Managing Member
address: 4812 Corvane Pkwy ste 207-300
N. Las Vegas, NV 89517
phone: (702) 555-0143
fax: (702) 555-0187
email: OakridgeHousePurchaser@examplemail.com
web: OakridgeHousePurchasers.example
*At the bottom of the card I would like....
We buy houses for cash....no repairs, no commissions, no fees!
Logo Text
OAKRIDGE HOUSE PURCHASERS "Investing in Our Community"
Font styles to use
Other font styles liked:
- Lora
Requirements
Must have
- On the back of the card, i'd like to have my logo large and the following statements:
- Are you considering selling your home? Want a simple, hassle-free transaction? We can help! We buy houses for cash and can close quickly! No need to do any repairs, no realtor commissions, no closing costs.....and no headaches. Let us help you with your real estate needs...!
Nice to have
- multiple colors 2 two tone on front and back

```html
<!DOCTYPE html>
<html lang="en">
<head>
<meta charset="utf-8">
<title>Oakridge House Purchasers – Business Card</title>
<link rel="stylesheet" href="https://fonts.googleapis.com/css2?family=Lora:wght@400;600&family=Open+Sans:wght@400;600&display=swap">
<style>
  :root {
    --blue: #0b6cc0;
    --blue-dark: #0a4f95;
    --blue-light: #1a86d6;
    --white: #ffffff;
    --paper: #f6f7f8;
    --grey: #d6d9dc;
    --ink: #3d4248;
    --bg: #e9e6e1;
  }
  * { box-sizing: border-box; margin: 0; padding: 0; }
  html, body { width: 1200px; height: 1023px; overflow: hidden; }
  body { background: var(--bg); position: relative; font-family: "Open Sans", Arial, sans-serif; }

  .card {
    position: absolute; left: 220px; width: 760px; height: 434px;
    border-radius: 18px; overflow: hidden;
    box-shadow: 0 8px 24px rgba(0,0,0,.18);
  }
  .card--front { top: 47px; background: linear-gradient(160deg, var(--white), var(--paper)); }
  .card--back { top: 542px; background: radial-gradient(ellipse at 55% 35%, var(--blue-light), var(--blue) 55%, var(--blue-dark)); }

  .front-wave { position: absolute; inset: 0; width: 100%; height: 100%; }

  .brand { position: absolute; left: 46px; top: 44px; display: flex; align-items: center; gap: 12px; }
  .brand__mark { width: 22px; height: 22px; background: var(--blue); }
  .brand__name { font-family: "Lora", Georgia, serif; font-weight: 600; color: var(--blue); font-size: 27px; line-height: 1.05; letter-spacing: .5px; }
  .slogan { position: absolute; left: 80px; top: 116px; font-family: "Lora", Georgia, serif; font-size: 13px; letter-spacing: 4px; color: var(--ink); }

  .person { position: absolute; right: 48px; top: 40px; text-align: right; }
  .person__name { font-size: 30px; color: var(--ink); font-weight: 400; }
  .person__role { font-size: 15px; color: var(--blue); margin-top: 2px; }

  .contacts { position: absolute; left: 46px; top: 240px; list-style: none; }
  .contacts li { display: flex; align-items: center; gap: 12px; font-size: 15px; color: var(--ink); height: 30px; }
  .contacts svg { width: 16px; height: 16px; fill: none; stroke: var(--blue); stroke-width: 1.6; }

  .address { position: absolute; right: 46px; bottom: 36px; text-align: right; color: var(--white); font-size: 15px; line-height: 1.5; font-weight: 600; }

  .back-logo { position: absolute; left: 0; right: 0; top: 118px; text-align: center; color: var(--white); }
  .back-logo__row { display: inline-flex; align-items: center; gap: 16px; }
  .back-logo__mark { width: 30px; height: 30px; background: var(--white); }
  .back-logo__name { font-family: "Lora", Georgia, serif; font-weight: 600; font-size: 48px; letter-spacing: 1px; line-height: 1.05; text-align: left; }
  .back-slogan { margin-top: 22px; font-family: "Lora", Georgia, serif; font-size: 18px; letter-spacing: 7px; }

  .back-strip { position: absolute; left: 0; right: 0; bottom: 0; height: 52px; background: var(--paper); display: flex; align-items: center; justify-content: center; font-size: 17px; color: var(--blue); letter-spacing: .3px; }
</style>
</head>
<body>

<section class="card card--front" aria-label="Card front">
  <svg class="front-wave" viewBox="0 0 760 434" preserveAspectRatio="none" aria-hidden="true">
    <path d="M320 434 C 430 420, 480 150, 760 100 L760 434 Z" fill="var(--grey)"/>
    <path d="M360 434 C 470 420, 510 170, 760 130 L760 434 Z" fill="var(--blue)"/>
  </svg>

  <div class="brand">
    <span class="brand__mark"></span>
    <span class="brand__name">OAKRIDGE<br>HOUSE PURCHASERS</span>
  </div>
  <p class="slogan">"Investing in Our Community"</p>

  <div class="person">
    <p class="person__name">Dale Pruitt</p>
    <p class="person__role">Managing Member</p>
  </div>

  <ul class="contacts">
    <li><svg viewBox="0 0 16 16"><circle cx="8" cy="8" r="7"/><path d="M5.5 5c0 3 2.5 5.5 5.5 5.5l.5-1.5-1.8-.8-.8.8c-1-.5-1.7-1.2-2.2-2.2l.8-.8L6.7 4.5z"/></svg>(702) 555-0143</li>
    <li><svg viewBox="0 0 16 16"><rect x="2" y="6" width="12" height="8"/><rect x="4" y="2" width="8" height="4"/><path d="M5 10h6"/></svg>(702) 555-0187</li>
    <li><svg viewBox="0 0 16 16"><rect x="1.5" y="3.5" width="13" height="9"/><path d="M1.5 3.5 8 9l6.5-5.5"/></svg>OakridgeHousePurchaser@examplemail.com</li>
    <li><svg viewBox="0 0 16 16"><circle cx="8" cy="8" r="6.5"/><ellipse cx="8" cy="8" rx="3" ry="6.5"/><path d="M1.5 8h13"/></svg>www.OakridgeHousePurchasers.example</li>
  </ul>

  <p class="address">4812 Corvane Pkwy ste 207-300<br>N. Las Vegas, NV 89517</p>
</section>

<section class="card card--back" aria-label="Card back">
  <div class="back-logo">
    <div class="back-logo__row">
      <span class="back-logo__mark"></span>
      <span class="back-logo__name">OAKRIDGE<br>HOUSE PURCHASERS</span>
    </div>
    <p class="back-slogan">"Investing in Our Community"</p>
  </div>
  <p class="back-strip">We buy houses for cash....no repairs, no commissions, no fees!</p>
</section>

</body>
</html>
```